THE MARKETPLACE FOR WAREHOUSE, the new way of doing logistics

We need an avant-garde, modern, minimalist and elegant web design for our company called VORDEN. This company represents the future of logistics, where users can find multiple offers of spaces (warehouse) in one place and other users can offer their available spaces to generate an extra cash inflow. A sample of this company is www.plindo-example.com, a US company that has developed this business. The closest thing to this type of business is NESTLOO, since it develops a similar model for people who offer spaces in their homes and people who need a space for a limited time. My domain site is www.vorden-example.com, where is the logo of my company. spanish- ------------------------------------------------ ---------------------------------------------- We need a web design avant-garde, modern, minimalist and elegant for our company called VORDEN. This company represents the future of logistics, where users can find multiple offers of spaces (wineries) in one place and other users can offer their available spaces to generate an extra profit. A sample of this company is www.plindo-example.com, a US company that has developed this business. The closest thing to this type of business is NESTLOO, since it develops a similar model for people who offer spaces in their homes and people who need a space for a limited time. My domain site is www.vorden-example.com, where is the logo of my company.

Target Market(s)

Companies, entrepreneurs, Companies, entrepreneurs,

Industry/Entity Type

Logistic

Number of Pages Required

5+ page

Colors
0d5aa6
ffffff
000000

Requirements
Must have
• A sober and minimalist homepage type quorbit, NstLoo. That is intuitive, must have spaces for advertising banners. You must always highlight the company logo. A sober and minimalist homepage like quorbit, NstLoo. That is intuitive, must have spaces for advertising banners. Must always highlight the company logo.

```html
<!DOCTYPE html>
<html lang="en">
<head>
<meta charset="utf-8">
<title>VORDEN — On-demand warehousing</title>
<link rel="stylesheet" href="https://fonts.googleapis.com/css2?family=Josefin+Sans:wght@400;600&family=EB+Garamond:wght@400&family=Roboto+Condensed:wght@400&display=swap">
<style>
:root{
  --brand-blue:#0d5aa6;
  --brand-blue-light:#2a7fd0;
  --white:#ffffff;
  --black:#000000;
  --ink:#1a1a1a;
  --footer-blue:#0d5aa6;
}
*{margin:0;padding:0;box-sizing:border-box}
html,body{width:1200px;height:2479px;overflow:hidden;background:var(--white)}
body{position:relative;font-family:"EB Garamond",Georgia,serif;color:var(--ink)}
.abs{position:absolute}
.display{font-family:"Josefin Sans",Arial,sans-serif}
.serif{font-family:"EB Garamond",Georgia,serif}

/* Hero */
.hero{left:0;top:0;width:1200px;height:674px;
  background:linear-gradient(100deg,#2c2724 0%,#5b5049 35%,#8a6f5f 60%,#4a2a2a 100%)}
.logo{left:116px;top:40px;display:flex;align-items:center;gap:14px}
.logo-dot{width:58px;height:58px;border-radius:50%;border:5px solid var(--brand-blue-light)}
.logo-name{font-family:"Josefin Sans",Arial,sans-serif;font-weight:600;font-size:52px;color:var(--brand-blue-light);letter-spacing:2px;line-height:1}
.nav{top:58px;font-family:"Roboto Condensed",Arial,sans-serif;font-size:22px;color:var(--white);white-space:nowrap}
.hero-kicker{left:197px;top:222px;font-size:26px;color:var(--white)}
.hero-title{left:197px;top:248px;font-size:46px;color:var(--brand-blue-light)}
.hero-copy{left:207px;top:302px;width:445px;font-size:19px;line-height:27px;color:var(--white)}
.hero-link{left:199px;top:442px;font-size:26px;color:var(--brand-blue-light)}

/* Features */
.heading{font-family:"Josefin Sans",Arial,sans-serif;color:var(--brand-blue);white-space:nowrap}
.body-copy{font-size:18px;line-height:26px;color:var(--black)}
.btn{display:flex;align-items:center;justify-content:center;background:var(--brand-blue);color:var(--white);
  font-family:"Josefin Sans",Arial,sans-serif;font-size:20px;border-radius:8px;height:43px}

/* Storage */
.storage-copy{width:465px;font-size:16px;line-height:22px;color:var(--black)}

/* Welcome band */
.welcome-band{left:0;top:1248px;width:1200px;height:521px;
  background:linear-gradient(180deg,#3a2519 0%,#4e3222 45%,#2e1c12 100%)}
.welcome-gifts{left:843px;top:1248px;width:357px;height:521px;
  background:linear-gradient(160deg,#e9d8c4 0%,#b5182a 35%,#8c1220 70%,#f1e6d6 100%)}
.welcome-title{left:215px;top:1316px;font-size:29px;color:var(--brand-blue)}
.welcome-copy{left:383px;top:1362px;width:400px;font-size:18px;line-height:23px;color:#f0e8e0}

/* Footer */
.footer{left:13px;top:2190px;width:1187px;height:289px;background:var(--footer-blue)}
.footer-title{top:2210px;font-family:"Josefin Sans",Arial,sans-serif;font-size:22px;color:var(--white);letter-spacing:.5px}
.footer-text{font-size:15px;line-height:22px;color:var(--white)}
.footer-links{font-family:"Josefin Sans",Arial,sans-serif;font-size:17px;line-height:24px;color:var(--white)}
</style>
</head>
<body>

<header>
  <div class="abs hero" role="img" aria-label="Photo of hands tying an orange ribbon around a gift box on a workbench"></div>
  <div class="abs logo"><span class="logo-dot"></span><span class="logo-name">VORDEN</span></div>
  <nav>
    <span class="abs nav" style="left:549px">HOME</span>
    <span class="abs nav" style="left:637px">SERVICES</span>
    <span class="abs nav" style="left:750px">TESTIMONIALS</span>
    <span class="abs nav" style="left:907px">ABOUT</span>
    <span class="abs nav" style="left:993px">CONTACT</span>
  </nav>
  <p class="abs display hero-kicker">Expicienda viventus et</p>
  <h1 class="abs display hero-title" style="font-weight:400">Need space?</h1>
  <p class="abs serif hero-copy">Nullam sodales, metus fringilla pharetra faucibus, elit ipsum bibendum arcu, id blandit mi neque ut dui. In eu pretium nisl. Vestibulum posuere ut ex non pellentesque. Lorem ipsum dolor sit amet, consectetur adipiscing elit.</p>
  <p class="abs display hero-link">et quod maximem</p>
</header>

<section class="features">
  <div class="abs" style="left:112px;top:736px;width:308px;height:349px;background:linear-gradient(180deg,#a9a59a 0%,#e3cfa8 45%,#8a5a33 100%)" role="img" aria-label="Photo of walnuts in a wooden crate"></div>
  <h3 class="abs heading" style="left:119px;top:1100px;font-size:19px;font-weight:400">Maximem ut sit quandum</h3>
  <p class="abs body-copy" style="left:119px;top:1126px;width:260px">Sed in dui in augue consectetur lobortis. Pellentesque orci tellus, imperdiet interdum nibh a, varius</p>

  <h3 class="abs heading" style="left:446px;top:764px;font-size:25px;font-weight:400">Et ipsum quodque</h3>
  <p class="abs body-copy" style="left:451px;top:804px;width:330px">Sed in dui in augue consectetur lobortis. Pellentesque orci tellus, imperdiet</p>
  <a class="abs btn" style="left:504px;top:879px;width:166px">read more</a>

  <h3 class="abs heading" style="left:446px;top:966px;font-size:25px;font-weight:400">Quomodo super</h3>
  <p class="abs body-copy" style="left:451px;top:1006px;width:330px">Sed in dui in augue consectetur lobortis. Pellentesque orci tellus, imperdiet</p>
  <a class="abs btn" style="left:504px;top:1101px;width:166px">read more</a>
  <p class="abs heading" style="left:451px;top:1174px;font-size:25px">Per existent est quod &gt;</p>

  <h3 class="abs heading" style="left:780px;top:744px;width:300px;font-size:25px;font-weight:400;line-height:36px;white-space:normal">Et ipsum quodque maximum</h3>
  <div class="abs" style="left:780px;top:818px;width:307px;height:251px;background:linear-gradient(180deg,#d9c7ae 0%,#9a4a2a 45%,#6e2a18 70%,#d6c3a8 100%)" role="img" aria-label="Photo of a vintage travel trunk with a brass clasp"></div>
  <h3 class="abs heading" style="left:780px;top:1082px;font-size:24px;font-weight:400">Per tuum signo</h3>
  <p class="abs body-copy" style="left:785px;top:1110px">Lorem ipsum dolor sit amet,</p>
  <a class="abs btn" style="left:838px;top:1154px;width:167px">read more</a>
</section>

<section class="welcome">
  <div class="abs welcome-band" role="img" aria-label="Photo of a dark wooden table top"></div>
  <div class="abs welcome-gifts" role="img" aria-label="Photo of red gift boxes tied with twine"></div>
  <h2 class="abs display welcome-title" style="font-weight:400">Welcome to our site</h2>
  <p class="abs serif welcome-copy">Donec pretium mattis augue vel bibendum. Mauris non nibh in tortor placerat pharetra. Nunc ut lacinia elit. Mauris nec ante ac quam dictum suscipit. Sed orci quam, fringilla vitae semper at, venenatis vel tellus. Suspendisse lacinia laoreet turpis et blandit. Pellentesque habitant morbi tristique senectus et netus et malesuada fames ac turpis egestas.</p>
  <a class="abs btn" style="left:622px;top:1575px;width:167px">read more</a>
</section>

<section class="storage">
  <div class="abs" style="left:112px;top:1810px;width:474px;height:281px;background:linear-gradient(120deg,#b9c3cc 0%,#e2c08a 40%,#c89b5c 70%,#f3f1ec 100%)" role="img" aria-label="Photo of a wooden kitchen storage caddy holding cutlery"></div>
  <h2 class="abs heading" style="left:615px;top:1820px;font-size:34px;font-weight:400">Perpit perplexa</h2>
  <p class="abs storage-copy" style="left:615px;top:1857px">Quisque tincidunt quam a porta sagittis. Etiam at urna dolor. Curabitur semper, arcu ut consequat sagittis, arcu purus venenatis est, et tristique nibh nibh porttitor odio. Nunc blandit ac ante in</p>
  <p class="abs heading" style="left:615px;top:1926px;font-size:22px">eternatitem magistima chose</p>
  <h2 class="abs heading" style="left:615px;top:1954px;font-size:34px;font-weight:400">Magis nihil verindum</h2>
  <p class="abs storage-copy" style="left:615px;top:1991px">Quisque tincidunt quam a porta sagittis. Etiam at urna dolor. Curabitur semper, arcu ut consequat sagittis, arcu purus venenatis est, et tristique nibh nibh porttitor odio. Nunc blandit ac ante in</p>
  <p class="abs heading" style="left:615px;top:2060px;font-size:22px">eternatitem magistima chose</p>
</section>

<footer>
  <div class="abs footer"></div>
  <h4 class="abs footer-title" style="left:116px;font-weight:400">ABOUT</h4>
  <p class="abs footer-text" style="left:116px;top:2244px;width:200px">Quisque fermentum non turpis at porttitor. Nulla interdum erat sed dui maximus, sit amet lacinia libero posuere. Cras bibendum maximus justo vitae rhoncus. Etiam non vulputate nulla. Aliquam vehicula velit vitae</p>

  <h4 class="abs footer-title" style="left:367px;font-weight:400">RESOURCES</h4>
  <p class="abs footer-links" style="left:367px;top:2244px">SERVICES<br>CONTACT<br>ABOUT US<br>TESTIMONIAL<br>PORTFOLIO<br>SPECIALITIES</p>

  <h4 class="abs footer-title" style="left:617px;font-weight:400">WHERE TO FIND US</h4>
  <p class="abs footer-text" style="left:617px;top:2244px">Street Lorem ipsum<br>Avenue dolor sit amet<br>Quod magis existerat, 27.<br>555010-010</p>

  <h4 class="abs footer-title" style="left:868px;font-weight:400">LOREM IPSUM</h4>
  <p class="abs footer-text" style="left:868px;top:2244px;width:200px">Quisque fermentum non turpis at porttitor. Nulla interdum erat sed dui maximus</p>
  <p class="abs footer-text" style="left:868px;top:2330px;width:200px">Cras bibendum maximus justo vitae rhoncus. Etiam non vulputate nulla.</p>
</footer>

</body>
</html>
```